Kelmora Legal Business Card

I require a corporate business card for a new legal services business.

I do not have a logo, nor do I want one.

I require a clean, neat a professional card for a law firm.

Details:

Business Name: Kelmora Legal
Name: Debra Lindqvist
Title: Corporate Services Manager
Location: Office 14 (Top Floor), Toravel Business Centre, Quinlan Grove Street, Alotau CBD, Milne Bay Province.
Postal Address: PO Box 593, Alotau, 211, Milne Bay Province, Papua New Guinea.
Contact: T: +675 6418250, F: +675 6413362, M: +675 72915867, E: dlindqvist@kelmoraexample.com.pg.

I look forward to your design submissions.

Industry/Entity Type

Legal

```html
<!DOCTYPE html>
<html lang="en">
<head>
<meta charset="utf-8">
<title>Kelmora Legal – Business Card</title>
<link rel="stylesheet" href="https://fonts.googleapis.com/css2?family=Libre+Baskerville:wght@700&family=Oswald:wght@400&family=Ubuntu:wght@400&display=swap">
<style>
  :root {
    --bg: #d6d6d6;
    --card: #ffffff;
    --card-edge: #ececec;
    --ink: #4a4a4a;
    --ink-soft: #6a6a6a;
    --rule: #3e3e3e;
  }
  * { box-sizing: border-box; margin: 0; padding: 0; }
  html, body { width: 1200px; height: 947px; overflow: hidden; }
  body {
    background: var(--bg);
    display: flex;
    align-items: center;
    justify-content: center;
    gap: 80px;
  }
  .card {
    position: relative;
    width: 400px;
    height: 700px;
    background: linear-gradient(160deg, var(--card) 0%, var(--card) 60%, var(--card-edge) 100%);
    border-radius: 30px;
    box-shadow: 0 6px 18px rgba(0,0,0,0.12);
  }
  .brand {
    position: absolute;
    left: 50px;
    top: 92px;
    font-family: "Libre Baskerville", serif;
    font-weight: 700;
    font-size: 34px;
    letter-spacing: 1px;
    color: var(--ink);
  }
  .detail {
    position: absolute;
    left: 40px;
    right: 24px;
    display: flex;
    align-items: center;
  }
  .detail--person  { top: 212px; }
  .detail--place   { top: 318px; }
  .detail--contact { top: 506px; }
  .detail__icon { width: 36px; height: 36px; flex: none; }
  .detail__rule {
    width: 4px;
    align-self: stretch;
    background: var(--rule);
    margin: 0 14px 0 12px;
    flex: none;
  }
  .detail__text {
    font-family: "Ubuntu", sans-serif;
    font-size: 13px;
    line-height: 1.5;
    letter-spacing: 0.6px;
    color: var(--ink);
  }
  .detail__group + .detail__group { margin-top: 8px; }
  .person-name {
    font-family: "Oswald", sans-serif;
    font-weight: 400;
    font-size: 28px;
    letter-spacing: 2px;
    line-height: 1.1;
    color: var(--ink);
  }
  .person-title {
    font-size: 13px;
    letter-spacing: 1px;
    color: var(--ink-soft);
  }
  .social {
    position: absolute;
    right: 34px;
    bottom: 34px;
    display: flex;
    gap: 18px;
    font-family: "Ubuntu", sans-serif;
    font-size: 12px;
    letter-spacing: 1px;
    color: var(--ink-soft);
  }
  .social__item { display: flex; align-items: center; gap: 6px; }
  .social__mark { width: 16px; height: 16px; background: var(--ink-soft); }
</style>
</head>
<body>
  <section class="card card--front" aria-label="Card front">
    <div class="brand">Kelmora Legal</div>

    <div class="detail detail--person">
      <svg class="detail__icon" viewBox="0 0 44 44" aria-hidden="true">
        <circle cx="22" cy="13" r="9" fill="var(--ink)"/>
        <path d="M5 42c0-10 7-17 17-17s17 7 17 17z" fill="var(--ink)"/>
      </svg>
      <span class="detail__rule"></span>
      <div class="detail__text">
        <div class="person-name">DEBRA LINDQVIST</div>
        <div class="person-title">Corporate Services Manager</div>
      </div>
    </div>

    <div class="detail detail--place">
      <svg class="detail__icon" viewBox="0 0 44 44" aria-hidden="true">
        <path d="M22 2c-8 0-14 6-14 14 0 10 14 26 14 26s14-16 14-26c0-8-6-14-14-14z" fill="var(--ink)"/>
        <circle cx="22" cy="16" r="5.5" fill="var(--card)"/>
      </svg>
      <span class="detail__rule"></span>
      <div class="detail__text">
        <div class="detail__group">
          Office 14 (Top Floor)<br>
          Toravel Business Centre<br>
          Quinlan Grove Street<br>
          Alotau CBD, Milne Bay Province
        </div>
        <div class="detail__group">
          PO Box 593, Alotau, 211<br>
          Milne Bay Province<br>
          Papua New Guinea
        </div>
      </div>
    </div>

    <div class="detail detail--contact">
      <svg class="detail__icon" viewBox="0 0 44 44" aria-hidden="true">
        <circle cx="22" cy="22" r="20" fill="var(--ink)"/>
        <g fill="none" stroke="var(--card)" stroke-width="2">
          <ellipse cx="22" cy="22" rx="9" ry="20"/>
          <line x1="22" y1="2" x2="22" y2="42"/>
          <line x1="2" y1="22" x2="42" y2="22"/>
          <path d="M6 12h32M6 32h32"/>
        </g>
      </svg>
      <span class="detail__rule"></span>
      <div class="detail__text">
        T: +675 6418250<br>
        F: +675 6413362<br>
        M: +675 72915867<br>
        E: dlindqvist@kelmoraexample.com.pg
      </div>
    </div>
  </section>

  <section class="card card--back" aria-label="Card back">
    <div class="social">
      <span class="social__item"><span class="social__mark"></span>linkfeed</span>
      <span class="social__item"><span class="social__mark"></span>chirper</span>
    </div>
  </section>
</body>
</html>
```